Print Ad for a Human Resource Company

Hi.
Apologies for the quick turnaround but I just was brought on board to handle this project. The publication is Coral Ridge Journal, a Hawaii Business & Lifestyle publication.
Their upcoming issue will feature HR companies & of course we want our ad to stand out from the rest & make the phone ring.

Size: Vertical Ad 2.5" x 9.875

Color: 4 color, non bleed

Format: Hi-res (300 dpi) pdf
Ad Due: Drop dead dealine is Friday, 1/04/2013

Color: 4 color, non bleed

Reason: There is a God in heaven. We have a stay on the deadline to January 4th.

Target Market(s)

Small companies that benefit from having experts handle these areas.

Industry/Entity Type

Business

Requirements
Must have
• Copy:
Tagline: Keeping It Simple
Accounting
Human Resources
Payroll Services
Employee Benefits
Commercial Insurance
Personal Insurance
No Hidden Fees

Photos of both owners:
Marisol Tenorio, CEO
Kara Wexley, President

Company logo
Address: 517 Harbor Crest Lane, Suite #204
Kalama Bay, HI 96788
Phone: 808.555.3172
BrightLedgerHub.com
Nice to have
• This is a small locally owned firm owned by 2 local, very smart, sophisticated yet approachable, hardworking women. Their colors are Black background, silver type. The ad should be a reflection of their personalities.

```html
<!DOCTYPE html>
<html lang="en">
<head>
<meta charset="utf-8">
<title>BrightLedger – Vertical Print Ad</title>
<link rel="stylesheet" href="https://fonts.googleapis.com/css2?family=Open+Sans:wght@400;700&family=Kaushan+Script&family=Arimo:wght@400&display=swap">
<style>
  :root {
    --stage-light: #c9c9c9;
    --stage-dark: #2a2a2c;
    --ad-black: #000000;
    --white: #ffffff;
    --silver: #d6d6d6;
    --ghost: #3b3b3b;
    --caption: #8c8c8c;
    --band-edge: #0a0a0a;
    --band-mid: #2b2627;
    --photo-light: #bdbdbd;
    --photo-dark: #2c2c2c;
  }
  * { box-sizing: border-box; margin: 0; padding: 0; }
  html, body { width: 1200px; height: 1000px; overflow: hidden; }
  body {
    position: relative;
    background: radial-gradient(ellipse at 50% 48%, var(--stage-dark) 0%, #6d6d6f 45%, var(--stage-light) 100%);
    font-family: "Open Sans", Arial, sans-serif;
  }
  .ad {
    position: absolute;
    left: 478px; top: 17px;
    width: 246px; height: 970px;
    background: var(--ad-black);
    border: 1px solid #555;
  }
  .ad > * { position: absolute; }

  .brand-name {
    left: 0; width: 100%;
    top: 22px;
    text-align: center;
    font-weight: 700;
    font-size: 22px;
    letter-spacing: 1px;
    color: var(--white);
  }
  .tagline {
    right: 32px; top: 52px;
    font-weight: 700;
    font-size: 14px;
    color: var(--white);
  }
  .brand-ghost {
    left: 0; width: 100%;
    top: 82px;
    text-align: center;
    font-weight: 700;
    font-size: 29px;
    letter-spacing: 0.5px;
    color: var(--ghost);
  }

  .services {
    left: 29px; top: 159px;
    list-style: none;
  }
  .services li {
    display: flex; align-items: center;
    height: 24.5px;
    font-family: "Kaushan Script", cursive;
    font-size: 17px;
    color: var(--silver);
    letter-spacing: 1.1px;
  }
  .services li::before {
    content: "";
    width: 5px; height: 5px;
    border: 1px solid var(--silver);
    margin-right: 6px;
    flex: none;
  }

  .owner-band {
    left: 9px; width: 227px; height: 88px;
    background: linear-gradient(90deg, var(--band-edge) 0%, var(--band-mid) 35%, var(--band-mid) 65%, var(--band-edge) 100%);
  }
  .owner-photo {
    left: 64px; width: 118px; height: 148px;
    background: radial-gradient(ellipse at 50% 35%, var(--photo-light) 0%, #8a8a8a 40%, var(--photo-dark) 100%);
  }
  .owner-name, .owner-title {
    left: 0; width: 100%;
    text-align: center;
    font-family: "Arimo", Arial, sans-serif;
    font-size: 14px;
    color: var(--caption);
  }
  .owner-title { letter-spacing: 0.5px; }

  .contact-heading {
    left: 16px; top: 816px;
    font-family: "Arimo", Arial, sans-serif;
    font-weight: 400;
    font-size: 15px;
    color: var(--caption);
  }
  .contact-line {
    left: 16px;
    font-size: 10.5px;
    line-height: 15px;
    color: var(--silver);
  }
  .footer-name {
    right: 12px; top: 945px;
    font-weight: 700;
    font-size: 11px;
    letter-spacing: 0.5px;
    color: var(--white);
  }
</style>
</head>
<body>
  <section class="ad" aria-label="BrightLedger vertical print advertisement">
    <div class="brand-name">BRIGHTLEDGER</div>
    <div class="tagline">Keeping It Simple</div>
    <div class="brand-ghost" aria-hidden="true">BRIGHTLEDGER</div>

    <ul class="services">
      <li>Accounting</li>
      <li>Human Resources</li>
      <li>Payroll Services</li>
      <li>Employee Benefits</li>
      <li>Commercial Insurance</li>
      <li>Personal Insurance</li>
      <li>No Hidden Fees</li>
    </ul>

    <div class="owner-band" style="top:418px"></div>
    <div class="owner-photo" style="top:388px" role="img" aria-label="Portrait photo of Kara Wexley, President"></div>
    <div class="owner-name" style="top:546px">Kara Wexley</div>
    <div class="owner-title" style="top:564px">PRESIDENT</div>

    <div class="owner-band" style="top:620px"></div>
    <div class="owner-photo" style="top:597px" role="img" aria-label="Portrait photo of Marisol Tenorio, CEO"></div>
    <div class="owner-name" style="top:755px">Marisol Tenorio</div>
    <div class="owner-title" style="top:773px">CEO</div>

    <h2 class="contact-heading">Contact Us</h2>
    <p class="contact-line" style="top:843px">517 Harbor Crest Lane, Suite #204<br>Kalama Bay, HI 96788</p>
    <p class="contact-line" style="top:887px">Phone: 808.555.3172</p>
    <p class="contact-line" style="top:916px">BrightLedgerHub.com</p>

    <div class="footer-name">BRIGHTLEDGER</div>
  </section>
</body>
</html>
```